Brightwave Reach - Business Card

We need a business card for a Social Media Marketing company that specializes in online marketing for small businesses in Canada using common Social Media platforms such as Pictora, Kinloop, Blinkit & Chirpo.

I have uploaded a copy of our logo which I would like utilized in the business card. We would like the business card to be modern yet classy design.

Our website is www.brightwavereach.ca

Industry/Entity Type

Marketing

Contact Information for Business Card

Email: info@brightwavereach.ca
Website: www.brightwavereach.ca
Telephone: 604-392-5108

Colors

Designer to choose colors to be used in the design.

Requirements
Must have
• Social Media icons on reverse
• Please add some designs with color.

```html
<!DOCTYPE html>
<html lang="en">
<head>
<meta charset="utf-8">
<title>Brightwave Reach – Business Card</title>
<link href="https://fonts.googleapis.com/css2?family=Source+Sans+3:wght@400;600;700&display=swap" rel="stylesheet">
<style>
  :root {
    --stage: #626262;
    --card-base: #000000;
    --band-light: #1e1e1e;
    --band-texture: #161616;
    --panel-mid: #0f0f0f;
    --panel-right: #121212;
    --chevron: #1a1a1a;
    --plate: #050505;
    --ink: #ffffff;
    --accent: #4ee9f1;
    --shadow: rgba(0,0,0,0.45);
  }
  html, body {
    margin: 0;
    padding: 0;
    width: 1120px;
    height: 1200px;
    overflow: hidden;
    background: var(--stage);
  }
  .stage {
    position: relative;
    width: 1120px;
    height: 1200px;
  }
  .card {
    position: absolute;
    left: 240px;
    width: 695px;
    height: 417px;
    display: block;
  }
  .card--front { top: 122px; }
  .card--back { top: 627px; }
  .card-shadow {
    position: absolute;
    left: 260px;
    width: 655px;
    height: 34px;
    border-radius: 50%;
    background: radial-gradient(ellipse at center, var(--shadow) 0%, rgba(0,0,0,0) 70%);
  }
  .card-shadow--front { top: 536px; }
  .card-shadow--back { top: 1041px; }
  .brand-text {
    font-family: "Source Sans 3", sans-serif;
    font-weight: 700;
    fill: var(--ink);
    letter-spacing: 1px;
  }
  .holder-name {
    font-family: "Source Sans 3", sans-serif;
    font-weight: 700;
    font-size: 40px;
    fill: var(--ink);
  }
  .holder-name .surname { fill: var(--accent); }
  .holder-role {
    font-family: "Source Sans 3", sans-serif;
    font-weight: 400;
    font-size: 27px;
    fill: var(--ink);
  }
  .contact-text {
    font-family: "Source Sans 3", sans-serif;
    font-weight: 600;
    font-size: 21px;
    fill: var(--ink);
  }
  .icon-disc { fill: var(--accent); }
  .icon-glyph { fill: none; stroke: #0b0b0b; stroke-width: 2.2; stroke-linejoin: round; stroke-linecap: round; }
  .icon-solid { fill: #0b0b0b; }
</style>
</head>
<body>
<main class="stage">

  <div class="card-shadow card-shadow--front"></div>
  <svg class="card card--front" viewBox="0 0 846 508" aria-label="Business card front">
    <rect width="846" height="508" fill="var(--card-base)"/>
    <!-- top band -->
    <rect x="0" y="28" width="846" height="100" fill="var(--band-light)"/>
    <polygon points="0,28 700,28 0,114" fill="var(--band-texture)"/>
    <polygon points="0,114 700,28 846,28 846,36 0,136" fill="var(--card-base)"/>
    <!-- middle panel -->
    <rect x="0" y="128" width="846" height="249" fill="var(--panel-mid)"/>
    <!-- bottom band -->
    <rect x="0" y="377" width="846" height="101" fill="var(--band-light)"/>
    <polygon points="0,468 846,364 846,382 110,478 0,478" fill="var(--card-base)"/>
    <polygon points="110,478 846,382 846,478" fill="var(--band-texture)"/>
    <!-- brand name -->
    <text class="brand-text" x="423" y="232" font-size="60" text-anchor="middle">BRIGHTWAVE</text>
    <text class="brand-text" x="423" y="292" font-size="60" text-anchor="middle">REACH</text>
  </svg>

  <div class="card-shadow card-shadow--back"></div>
  <svg class="card card--back" viewBox="0 0 846 508" aria-label="Business card back">
    <rect width="846" height="508" fill="var(--card-base)"/>
    <!-- top band -->
    <rect x="0" y="28" width="846" height="100" fill="var(--band-light)"/>
    <polygon points="0,28 700,28 0,114" fill="var(--band-texture)"/>
    <polygon points="0,114 700,28 846,28 846,36 0,136" fill="var(--card-base)"/>
    <!-- middle panel -->
    <rect x="0" y="128" width="846" height="249" fill="var(--panel-mid)"/>
    <polygon points="428,128 846,128 846,377 420,377 365,253" fill="var(--panel-right)"/>
    <polyline points="428,128 365,253 420,377" fill="none" stroke="var(--chevron)" stroke-width="6"/>
    <!-- bottom band -->
    <rect x="0" y="377" width="846" height="101" fill="var(--band-light)"/>
    <polygon points="0,468 846,364 846,382 110,478 0,478" fill="var(--card-base)"/>
    <polygon points="110,478 846,382 846,478" fill="var(--band-texture)"/>

    <!-- small brand name -->
    <text class="brand-text" x="753" y="78" font-size="17" text-anchor="middle">BRIGHTWAVE</text>
    <text class="brand-text" x="753" y="97" font-size="17" text-anchor="middle">REACH</text>

    <!-- name plate -->
    <rect x="-10" y="207" width="355" height="90" rx="5" fill="var(--plate)"/>
    <text class="holder-name" x="293" y="252" text-anchor="end">JOHN <tspan class="surname">SMITH</tspan></text>
    <text class="holder-role" x="293" y="279" text-anchor="end">DATA &amp; DESIGN</text>

    <!-- contact: email -->
    <g class="contact-row">
      <circle class="icon-disc" cx="467" cy="164" r="18"/>
      <rect class="icon-glyph" x="457" y="157" width="20" height="14" rx="1.5"/>
      <polyline class="icon-glyph" points="457,158 467,166 477,158"/>
      <text class="contact-text" x="500" y="172">info@brightwavereach.ca</text>
    </g>
    <!-- contact: web -->
    <g class="contact-row">
      <circle class="icon-disc" cx="467" cy="222" r="18"/>
      <circle class="icon-glyph" cx="467" cy="222" r="10"/>
      <ellipse class="icon-glyph" cx="467" cy="222" rx="4.5" ry="10"/>
      <line class="icon-glyph" x1="457" y1="222" x2="477" y2="222"/>
      <text class="contact-text" x="500" y="230">www.brightwavereach.ca</text>
    </g>
    <!-- contact: phone -->
    <g class="contact-row">
      <circle class="icon-disc" cx="467" cy="281" r="18"/>
      <path class="icon-solid" d="M459,271 l5,-1 l3,7 l-3,3 q2,5 7,7 l3,-3 l7,3 l-1,5 q-2,2 -5,2 q-16,-3 -19,-19 q0,-3 3,-4z"/>
      <text class="contact-text" x="499" y="289">604-392-5108</text>
    </g>
    <!-- contact: address -->
    <g class="contact-row">
      <circle class="icon-disc" cx="467" cy="341" r="18"/>
      <path class="icon-solid" d="M467,354 q-9,-10 -9,-17 a9,9 0 0 1 18,0 q0,7 -9,17z"/>
      <circle cx="467" cy="337" r="3.5" fill="var(--accent)"/>
      <text class="contact-text" x="499" y="349">your Address goes here</text>
    </g>
  </svg>

</main>
</body>
</html>
```